New Fun, Positive, energised looking Business Card Needed for High Achiever Coach

I am looking for a two sided full colour business card. I am self employed and have recently re branded my 1-2-1 work re-vitalising high achievers. My target client base for these cards is therefore high achievers - usually aged 40 -55, they are often entrepreneurs, CEO or work in banking and finance and 2/3 are male. I work with them on 90 day or 6 month coaching programs to help them live their success in a healthier, more sustainable and fulfiiled way. They pay for this privately so though they are corporate types the cards need not look 'corporate'. I want to portray the idea of transformation, vitality and re-connecting.
You can get a feel for the look I like on my new website: corinvale.co.uk
I want to use this logo with strapline (Re-Vitalising High Achievers) (I purchased off Logoharbor) and font/ colours (the turquoise and green).
Details to include on the card:
www.corinvale.co.uk
+44 7915 264318
mira@corinvale.co.uk
skype: miracorin
I'd also like to include:
Do you struggle to switch off? Want to be healthier and feel fitter? Want closer relationships? More clarity over the direction you are headed? I can help you do these things using integrated mind-body techniques. Visit corinvale.co.uk TODAY to apply for a FREE Breakthrough session.
BUT if that is too much text for a card I am open to advice/ammendments.
Updates
Thanks for your design - I am considering them. PLease change the wording to :

```html
<!DOCTYPE html>
<html lang="en">
<head>
<meta charset="utf-8">
<title>Mira Corin – Business Card</title>
<link rel="stylesheet" href="https://fonts.googleapis.com/css2?family=Nunito+Sans:ital,wght@0,400;0,800;1,300;1,400&display=swap">
<style>
  :root {
    --backdrop: #1b1b1b;
    --card-light: #f6f6f6;
    --card-shade: #dcdcdc;
    --turquoise: #36a3cf;
    --leaf-green: #6cb85d;
    --ink: #232323;
    --band-top: #b3d6f0;
    --band-bottom: #79ade0;
  }
  * { box-sizing: border-box; margin: 0; padding: 0; }
  html, body {
    width: 1134px; height: 1200px; overflow: hidden;
    background: var(--backdrop);
    font-family: "Nunito Sans", sans-serif;
  }
  .card {
    position: absolute; left: 97px; width: 918px;
    background: radial-gradient(ellipse at 60% 35%, var(--card-light) 0%, #ececec 55%, var(--card-shade) 100%);
    overflow: hidden;
  }
  .card--front { top: 58px; height: 524px; }
  .card--back { top: 629px; height: 526px; }

  .brand { position: absolute; text-align: center; }
  .brand__dot { display: block; margin: 0 auto; border-radius: 50%; background: var(--leaf-green); }
  .brand__name { color: var(--turquoise); font-weight: 800; line-height: 1; white-space: nowrap; }
  .brand__strapline { color: var(--turquoise); font-style: italic; font-weight: 400; white-space: nowrap; }

  .card--front .brand { left: 0; width: 100%; top: 200px; }
  .card--front .brand__dot { width: 56px; height: 56px; margin-bottom: 58px; }
  .card--front .brand__name { font-size: 42px; }
  .card--front .brand__strapline { font-size: 21px; margin-top: 8px; }

  .pitch {
    position: absolute; left: 45px; top: 104px; width: 640px;
    font-size: 23px; line-height: 30px; font-style: italic; font-weight: 300;
    color: var(--ink);
  }

  .card--back .brand { left: 640px; width: 230px; top: 195px; }
  .card--back .brand__dot { width: 36px; height: 36px; margin-bottom: 64px; }
  .card--back .brand__name { font-size: 27px; }
  .card--back .brand__strapline { font-size: 14px; margin-top: 4px; }

  .contact-band {
    position: absolute; left: 0; top: 380px; width: 100%; height: 101px;
  }
  .contact-band svg { position: absolute; inset: 0; }
  .contact-list {
    position: absolute; left: 34px; top: 32px;
    display: grid; grid-template-columns: 264px auto; row-gap: 4px;
    font-size: 22px; line-height: 26px; color: var(--ink);
  }
  .card__shadow {
    position: absolute; left: 100px; top: 484px; width: 718px; height: 10px;
    border-radius: 50%;
    background: radial-gradient(ellipse at center, rgba(0,0,0,0.45), rgba(0,0,0,0) 70%);
  }
</style>
</head>
<body>
  <section class="card card--front">
    <div class="brand">
      <span class="brand__dot"></span>
      <p class="brand__name">Mira Corin</p>
      <p class="brand__strapline">Re-Vitalising High Achievers</p>
    </div>
  </section>

  <section class="card card--back">
    <p class="pitch">Do you struggle to switch off? Want to be healthier and feel fitter? Want closer relationships? More clarity over the direction you are headed? I can help you do these things using integrated mind-body techniques. Visit corinvale.co.uk TODAY to apply for a FREE Breakthrough session.</p>

    <div class="brand">
      <span class="brand__dot"></span>
      <p class="brand__name">Mira Corin</p>
      <p class="brand__strapline">Re-Vitalising High Achievers</p>
    </div>

    <div class="contact-band">
      <svg width="918" height="101" viewBox="0 0 918 101" aria-hidden="true">
        <defs>
          <linearGradient id="band-fill" x1="0" y1="0" x2="0" y2="1">
            <stop offset="0" stop-color="var(--band-top)"/>
            <stop offset="1" stop-color="var(--band-bottom)"/>
          </linearGradient>
        </defs>
        <path d="M0 17 H735 C745 17 748 2 755 2 C762 2 765 17 775 17 H918 V101 H0 Z" fill="url(#band-fill)"/>
      </svg>
      <div class="contact-list">
        <span>www.corinvale.co.uk</span><span>mira@corinvale.co.uk</span>
        <span>+44 7915 264318</span><span>skype: miracorin</span>
      </div>
    </div>
    <div class="card__shadow"></div>
  </section>
</body>
</html>
```